BUSINESS CONSULTING

Would like a page design that would reflect "flow" effect that denotes moving around obstacles and logo webpage for BREXA Consulting. We provide business consulting in the areas of training/facilitation, Leadership Coaching and Development, Process Improvement and Employee On-boarding and Authorization.

Need skeletal designed to be populated at a later date.

```html
<!DOCTYPE html>
<html lang="en">
<head>
<meta charset="utf-8">
<title>BREXA Consulting</title>
<link href="https://fonts.googleapis.com/css2?family=PT+Sans:wght@400;700&family=Roboto+Condensed:wght@700&display=swap" rel="stylesheet">
<style>
:root{
  --blue:#0a79b8;
  --blue-dark:#05527e;
  --blue-nav-top:#1f8cc8;
  --red:#d20a0a;
  --text:#2b2b2b;
  --grey-head:#6a6a6a;
  --hero-bg:#f4f4f4;
  --body-bg:#e4e4e4;
  --btn-grey:#9a9a9a;
  --footer:#0a7bbb;
  --footer-brand:#8fc9ea;
}
*{margin:0;padding:0;box-sizing:border-box}
html,body{width:1200px;height:1140px;overflow:hidden}
body{font-family:"PT Sans",sans-serif;color:var(--text);background:var(--body-bg);position:relative}
.wrap{position:absolute;left:150px;width:900px}

.site-header{position:absolute;top:0;left:0;width:1200px;height:93px;background:#fff}
.brand{left:150px;top:24px;display:flex;align-items:center;gap:8px;font-weight:700;font-size:32px;color:var(--blue);letter-spacing:.3px}
.brand-square{width:14px;height:14px;background:var(--blue)}
.header-phone{position:absolute;right:150px;top:40px;display:flex;align-items:center;gap:10px;font-family:"Roboto Condensed",sans-serif;font-weight:700;font-size:23px;color:var(--blue)}
.phone-badge{width:26px;height:26px;border-radius:4px;background:var(--red);display:flex;align-items:center;justify-content:center}

.main-nav{position:absolute;top:93px;left:0;width:1200px;height:37px;background:linear-gradient(var(--blue-nav-top),var(--blue-dark))}
.main-nav ul{list-style:none;display:flex;position:absolute;left:150px;top:0;height:37px;border-left:1px solid rgba(255,255,255,.25)}
.main-nav li{height:37px;display:flex;align-items:center;padding:0 20px;border-right:1px solid rgba(255,255,255,.25);color:#fff;font-family:Arial,sans-serif;font-weight:700;font-size:12px;letter-spacing:.3px}
.main-nav li:first-child{padding:0 21px 0 28px}

.hero{position:absolute;top:130px;left:0;width:1200px;height:449px;background:var(--hero-bg)}
.slide-frame{position:absolute;left:150px;top:28px;width:900px;height:384px;background:#fff;padding:5px;box-shadow:0 14px 14px -10px rgba(0,0,0,.35)}
.slide-image{width:100%;height:100%;background:linear-gradient(100deg,#e9c79a 0%,#cfc5b8 30%,#8fb0d2 60%,#1f5fb9 100%);position:relative}
.slide-image::after{content:"";position:absolute;left:0;right:0;bottom:0;height:38%;background:linear-gradient(transparent,rgba(120,70,40,.55))}
.slide-caption{position:absolute;left:0;right:0;top:268px;text-align:center;color:#fff;font-size:21px;line-height:34px;z-index:1;text-shadow:0 1px 3px rgba(0,0,0,.4)}
.slide-caption b{font-size:27px}
.slide-arrow{position:absolute;top:189px}
.slide-arrow.prev{left:86px}
.slide-arrow.next{right:86px}

.services{top:608px;display:flex}
.service{width:225px;height:255px;padding:0 8px 0 12px;border-left:1px dotted #888;position:relative}
.service:first-child{border-left:none;padding-left:2px;width:216px}
.service h2{font-size:18px;line-height:18px;color:var(--blue);font-weight:700;text-transform:uppercase}
.service h2 span{display:block;color:var(--grey-head);text-transform:none;font-size:18px}
.service p{font-size:12.5px;line-height:17px;margin-top:18px}
.service ul{list-style:none;margin-top:9px}
.service li{font-size:12.5px;line-height:15.5px;color:var(--blue);padding-left:12px;position:relative;margin-bottom:7px}
.service li::before{content:"";position:absolute;left:0;top:4px;width:5px;height:5px;border-right:1.5px solid var(--blue);border-top:1.5px solid var(--blue);transform:rotate(45deg)}
.btn{position:absolute;left:0;top:208px;height:26px;padding:0 11px;border-radius:2px;background:var(--btn-grey);color:#fff;font-size:11px;font-weight:700;line-height:26px}
.service:not(:first-child) .btn{left:12px}
.btn.active{background:var(--red)}

.divider{top:868px;border-top:1px dotted #888}
.who{position:absolute;left:150px;top:897px;width:630px}
.section-title{font-size:24px;font-weight:400;color:var(--blue);letter-spacing:.3px}
.who p{font-size:12.5px;line-height:16px;margin-top:14px}
.who p+p{margin-top:16px}
.contact{position:absolute;left:834px;top:897px;width:220px}
.contact ul{list-style:none;margin-top:14px}
.contact li{display:flex;gap:14px;font-size:12.5px;line-height:16px;margin-bottom:13px}
.contact li svg{flex:none;margin-top:1px}

.site-footer{position:absolute;top:1071px;left:0;width:1200px;height:69px;background:var(--footer);color:#fff}
.footer-nav{position:absolute;left:151px;top:13px;font-size:13px}
.footer-nav span{margin:0 7px}
.copyright{position:absolute;left:151px;top:34px;font-size:13px}
.footer-brand{position:absolute;right:150px;top:14px;font-weight:700;font-size:30px;color:var(--footer-brand)}
</style>
</head>
<body>
<header class="site-header">
  <div class="wrap brand"><span class="brand-square"></span>BREXA Consulting</div>
  <div class="header-phone">
    <span class="phone-badge"><svg width="16" height="16" viewBox="0 0 24 24"><path fill="#fff" d="M6.6 10.8a15.1 15.1 0 0 0 6.6 6.6l2.2-2.2c.3-.3.7-.4 1-.2 1.1.4 2.3.6 3.6.6.6 0 1 .4 1 1V20c0 .6-.4 1-1 1A17 17 0 0 1 3 4c0-.6.4-1 1-1h3.5c.6 0 1 .4 1 1 0 1.3.2 2.5.6 3.6.1.3 0 .7-.2 1z"/></svg></span>
    404-555-0182
  </div>
</header>

<nav class="main-nav">
  <ul>
    <li>HOME</li><li>ABOUT US</li><li>OUR SERVICES</li><li>PARTNERSHIP OVERVIEW</li><li>CONTACT US</li>
  </ul>
</nav>

<section class="hero">
  <svg class="slide-arrow prev" width="36" height="70" viewBox="0 0 36 70"><path d="M35 1 1 35l34 34" fill="none" stroke="#c8c8c8" stroke-width="2"/></svg>
  <div class="slide-frame">
    <div class="slide-image" role="img" aria-label="Photo conveying flow and motion, warm sunset tones blending into blue sky">
      <p class="slide-caption"><b>BREXA CONSULTING, LLC</b> is an Atlanta based full service<br><b>BUSINESS CONSULTING</b> service provider</p>
    </div>
  </div>
  <svg class="slide-arrow next" width="36" height="70" viewBox="0 0 36 70"><path d="M1 1l34 34L1 69" fill="none" stroke="#c8c8c8" stroke-width="2"/></svg>
</section>

<section class="wrap services">
  <article class="service">
    <h2>Training<span>Facilitation Services</span></h2>
    <p>Our facilitators deliver hands-on training programs for teams of every size.</p>
    <ul><li>Workshops</li><li>Seminars</li><li>Online courses</li><li>Team sessions</li></ul>
    <span class="btn">READ MORE</span>
  </article>
  <article class="service">
    <h2>Leadership<span>Coaching &amp; Development</span></h2>
    <p>Our coaching helps leaders grow with clarity and confidence.</p>
    <ul><li>Executive Coaching</li><li>Leadership Development</li><li>Team Building</li></ul>
    <span class="btn">READ MORE</span>
  </article>
  <article class="service">
    <h2>Process Improvement<span>&amp; Consulting Services</span></h2>
    <p>Our structured approach finds business efficiency and improvement opportunities.</p>
    <ul><li>Industry best practices</li><li>Business improvement opportunity assessments</li><li>Financial impact assessments</li></ul>
    <span class="btn active">READ MORE</span>
  </article>
  <article class="service">
    <h2>On-boarding<span>Employee Authorization</span></h2>
    <p>Our programs bring new hires up to speed quickly, clearly and securely.</p>
    <ul><li>Orientation programs</li><li>Role-based access authorization</li><li>Compliance training</li></ul>
    <span class="btn">READ MORE</span>
  </article>
</section>

<div class="wrap divider"></div>

<section class="who">
  <h2 class="section-title">WHO WE ARE</h2>
  <p>Lorem ipsum dolor sit amet, consectetur adipiscing elit. Nunc iaculis purus nec massa commodo pellentesque. Sed lobortis nisi ligula, in ullamcorper eros vulputate eget. Sed sit amet erat gravida, auctor nisi vitae, placerat odio. Integer aliquam adipiscing semper.</p>
  <p>Maecenas non nunc scelerisque ipsum fermentum dignissim a a libero. Cum sociis natoque penatibus et magnis dis parturient montes, nascetur ridiculus mus.</p>
</section>

<section class="contact">
  <h2 class="section-title">CONTACT US</h2>
  <ul>
    <li><svg width="12" height="14" viewBox="0 0 12 14"><path d="M6 0a5 5 0 0 0-5 5c0 3.5 5 9 5 9s5-5.5 5-9a5 5 0 0 0-5-5zm0 7a2 2 0 1 1 0-4 2 2 0 0 1 0 4z" fill="#d20a0a"/></svg><span>Lorem ipsum dolor sit amet,<br>BREXA Consulting, LLC</span></li>
    <li><svg width="12" height="14" viewBox="0 0 24 24"><path fill="#d20a0a" d="M6.6 10.8a15.1 15.1 0 0 0 6.6 6.6l2.2-2.2c.3-.3.7-.4 1-.2 1.1.4 2.3.6 3.6.6.6 0 1 .4 1 1V20c0 .6-.4 1-1 1A17 17 0 0 1 3 4c0-.6.4-1 1-1h3.5c.6 0 1 .4 1 1 0 1.3.2 2.5.6 3.6.1.3 0 .7-.2 1z"/></svg><span>404-555-0182</span></li>
    <li><svg width="13" height="10" viewBox="0 0 13 10"><rect width="13" height="10" fill="#d20a0a"/><path d="M0 0l6.5 5L13 0" fill="none" stroke="#fff" stroke-width="1"/></svg><span>info@brexamail.com</span></li>
  </ul>
</section>

<footer class="site-footer">
  <div class="footer-nav">Home<span>|</span>About us<span>|</span>Our Services<span>|</span>Partnership Overview<span>|</span>Contact us</div>
  <div class="copyright">Copyright © 2014 BREXA Consulting, LLC</div>
  <div class="footer-brand">BREXA</div>
</footer>
</body>
</html>
```